Thai Restaurant Billboard Design

Design a billboard promoting food delivery during this Coronavirus time. We want to grab attention by embracing the Coronavirus and offering food delivery. People are sitting at home and this is the right time to promote food delivery.

I have the logo and spec sheet attached.

Target Market(s)

Anyone.

Requirements
Must have
• Top Heading should be big and bold:

Coronavirus Got You Quarantined?

Then put under

We Deliver
Healthy Thai Food!
Put the logo that is attached
415-283-6071
Nice to have
• Eyecatching. Creative.
Should not have
• Don't have any not haves. Make it look good.

```html
<!DOCTYPE html>
<html lang="en">
<head>
<meta charset="utf-8">
<title>Siam Lotus House – Delivery Billboard</title>
<link rel="stylesheet" href="https://fonts.googleapis.com/css2?family=Poppins:ital,wght@0,600;0,700;1,800&family=Bebas+Neue&family=Open+Sans:wght@700&display=swap">
<style>
  :root {
    --canvas: #ffffff;
    --board-bg: #ececec;
    --ink: #111111;
    --ink-soft: #333333;
    --phone-ink: #3a3a3a;
    --brand-ink: #4a4a4a;
    --accent-yellow: #f4d313;
    --food-warm: #d9b77a;
    --food-light: #f3ecdc;
  }
  * { margin: 0; padding: 0; box-sizing: border-box; }
  html, body {
    width: 1200px; height: 1200px; overflow: hidden;
    background: var(--canvas);
  }
  .canvas { position: relative; width: 1200px; height: 1200px; }

  .billboard {
    position: absolute; left: 64px; top: 423px;
    width: 1073px; height: 354px;
    background: var(--board-bg);
    overflow: hidden;
  }
  .billboard__pattern {
    position: absolute; inset: 0;
    background: linear-gradient(180deg, #efefef 0%, #e6e6e6 100%);
  }

  .headline { position: absolute; font-family: "Poppins", sans-serif; font-style: italic; font-weight: 800; line-height: 1; }
  .headline--virus { left: 76px; top: 50px; font-size: 58px; color: var(--ink); letter-spacing: -0.5px; }
  .headline--got-you { left: 62px; top: 106px; font-size: 86px; color: var(--accent-yellow); letter-spacing: -6px; }
  .headline--quarantined { left: 102px; top: 198px; font-size: 37px; color: var(--ink); letter-spacing: -0.5px; }

  .tagline {
    position: absolute; left: 44px; top: 266px;
    font-family: "Bebas Neue", sans-serif; font-size: 44px;
    color: var(--ink-soft); letter-spacing: 0.3px; line-height: 1;
  }

  .dish-photo {
    position: absolute; left: 425px; top: 82px;
    width: 390px; height: 230px;
    border-radius: 50%;
    background: radial-gradient(ellipse at 50% 45%, var(--food-warm) 0%, #e5cfa0 45%, var(--food-light) 75%, #f7f5f0 100%);
  }

  .brand {
    position: absolute; left: 846px; top: 40px; width: 200px;
    text-align: center;
    font-family: "Poppins", sans-serif; font-weight: 600;
    color: var(--brand-ink);
  }
  .brand__mark {
    width: 110px; height: 110px; margin: 0 auto 14px;
    background: var(--brand-ink);
  }
  .brand__name { font-size: 19px; line-height: 1.2; }
  .brand__sub { font-size: 13px; line-height: 1.3; }

  .phone {
    position: absolute; left: 730px; top: 292px;
    font-family: "Open Sans", sans-serif; font-weight: 700;
    font-size: 40px; color: var(--phone-ink); letter-spacing: 1px; line-height: 1;
  }
</style>
</head>
<body>
  <main class="canvas">
    <section class="billboard">
      <div class="billboard__pattern" role="img" aria-label="Light grey Thai damask ornament pattern background"></div>

      <h1 class="headline headline--virus">Coronavirus</h1>
      <p class="headline headline--got-you">GOT YOU</p>
      <p class="headline headline--quarantined">Quarantined?</p>

      <p class="tagline">We Deliver Healthy Thai Food!</p>

      <div class="dish-photo" role="img" aria-label="Photo of a plate of pad thai with tofu, bean sprouts, carrot and lime"></div>

      <div class="brand">
        <div class="brand__mark"></div>
        <p class="brand__name">Siam Lotus House</p>
        <p class="brand__sub">Restaurant</p>
      </div>

      <p class="phone">415-283-6071</p>
    </section>
  </main>
</body>
</html>
```